Brevanor Inc. Website

We need a website design for a new company based in Montreal, Canada. Our company offers professional services in planning & scheduling for major construction projects in varying industries. The main colors to be used are black & red (same as in logo). The final design should convey professionalism, precision, and excellence. The following are examples of what the website layout could look like: https://www.quilvardo.ca/, https://7496.ca/, https://lumavikt.ca/, https://www.dremorhext.com/en. Avoid using stock videos or photos with people in it.
Target audience are multi-national clients looking to hire a firm to manage their construction projects. Target market is Mining & Metals
Mining & Metalurgy, Hydroelectricity, Infrastructure
1 page

```html
<!DOCTYPE html>
<html lang="en">
<head>
<meta charset="utf-8">
<title>Brevanor Inc. — Planning &amp; Scheduling</title>
<link href="https://fonts.googleapis.com/css2?family=Space+Grotesk:wght@400;500;600;700&family=Inter:wght@400;500&display=swap" rel="stylesheet">
<style>
:root{
  --red:#a30f24;
  --red-dark:#860b1c;
  --ink:#222222;
  --charcoal:#3b3b3b;
  --muted:#6f6f6f;
  --line:#d9d9d9;
  --paper:#ffffff;
  --footer:#3a3a3a;
}
*{box-sizing:border-box;margin:0;padding:0}
html,body{width:1200px;height:2432px;overflow:hidden;background:var(--paper)}
body{position:relative;font-family:"Inter",sans-serif;color:var(--ink)}
.head,.title{font-family:"Space Grotesk",sans-serif}
.abs{position:absolute}

/* header */
.site-header{left:0;top:0;width:1200px;height:144px}
.brand{display:flex;align-items:center;gap:10px;font-family:"Space Grotesk",sans-serif;font-weight:700;font-size:22px;color:var(--red);white-space:nowrap}
.brand-dot{width:18px;height:18px;border-radius:50%;background:var(--red)}
.site-header .brand{position:absolute;left:272px;top:90px}
.nav{display:flex;gap:22px;font-family:"Space Grotesk",sans-serif;font-size:13px;color:var(--ink);white-space:nowrap}
.nav a{color:inherit;text-decoration:none}
.nav .active{color:var(--red);border-bottom:2px solid var(--red);padding-bottom:4px}
.site-header .nav{position:absolute;left:580px;top:96px}

/* hero */
.hero{left:0;top:144px;width:1200px;height:496px;background:linear-gradient(110deg,#f2c6a8 0%,#e9a27e 35%,#c9785e 60%,#6d6a78 100%)}
.hero h1{position:absolute;left:272px;top:148px;font-family:"Space Grotesk",sans-serif;font-weight:600;font-size:46px;line-height:54px;color:var(--ink)}
.btn{display:inline-flex;align-items:center;gap:10px;background:var(--red);color:#fff;font-family:"Space Grotesk",sans-serif;font-size:14px;padding:12px 22px;white-space:nowrap}
.hero .btn{position:absolute;left:272px;top:292px}

/* features */
.feature{width:160px;height:140px;background:var(--red);color:#fff;text-align:center;padding:22px 14px}
.feature.dark{background:var(--charcoal);height:200px;padding-top:48px}
.feature svg{display:block;margin:0 auto 10px}
.feature h3{font-family:"Space Grotesk",sans-serif;font-size:13px;font-weight:600;margin-bottom:6px}
.feature p{font-size:9px;line-height:13px;opacity:.85}

/* labels */
.eyebrow{font-family:"Space Grotesk",sans-serif;font-size:10px;font-weight:600;letter-spacing:1px;color:var(--red);text-transform:uppercase}
.section-title{font-family:"Space Grotesk",sans-serif;font-weight:600;font-size:34px;line-height:40px;color:var(--ink)}
.body-copy{font-size:10px;line-height:15px;color:var(--muted)}

/* about */
.about-mark{left:660px;top:820px;width:240px;height:190px;display:flex;align-items:center;justify-content:center}
.about-mark .brand{font-size:40px;gap:16px}
.about-mark .brand-dot{width:36px;height:36px}

/* services */
.service{width:158px;height:248px;background:var(--charcoal);color:#fff;padding:18px 12px}
.service.red{background:var(--red)}
.service h3{font-family:"Space Grotesk",sans-serif;font-weight:600;font-size:20px;line-height:22px;margin-bottom:14px}
.service p{font-size:10px;line-height:15px;opacity:.85}

/* testimonials */
.client-photo{left:312px;top:1560px;width:200px;height:190px;background:linear-gradient(170deg,#6fa3b8 0%,#9bbfca 60%,#c7b79c 100%)}
.quote-box{left:532px;top:1568px;width:40px;height:40px;background:var(--red);display:flex;align-items:center;justify-content:center}
.dots{display:flex;gap:6px}
.dots span{width:8px;height:8px;border-radius:50%;background:var(--line)}
.dots span.on{background:var(--red)}

/* form */
.field{height:30px;border:1px solid var(--line);font-size:10px;color:#9a9a9a;padding:9px 10px;display:flex;justify-content:space-between;align-items:center}
.field.area{height:84px;align-items:flex-start}
.map{left:660px;top:1840px;width:268px;height:280px;background:linear-gradient(135deg,#e7ebee 0%,#d6e0e6 50%,#b9d0df 100%)}
.address-card{left:660px;top:2120px;width:268px;height:100px;border-top:3px solid var(--red);background:#fff;box-shadow:0 4px 14px rgba(0,0,0,.08);padding:16px 20px}
.contact-item{display:flex;gap:10px;align-items:flex-start;font-size:10px;line-height:15px;color:var(--ink)}
.icon-circle{width:26px;height:26px;border-radius:50%;background:var(--ink);display:flex;align-items:center;justify-content:center;flex:none}

/* footer */
.site-footer{left:0;top:2260px;width:1200px;height:172px;background:var(--footer);color:#fff}
.site-footer .brand{position:absolute;left:272px;top:74px;color:#fff;font-size:18px;gap:8px}
.site-footer .brand-dot{background:var(--red);width:14px;height:14px}
.site-footer .copy{position:absolute;left:400px;top:80px;width:230px;font-size:9px;color:#cfcfcf;white-space:nowrap}
.site-footer .nav{position:absolute;left:680px;top:76px;color:#fff;font-size:12px;gap:20px}
</style>
</head>
<body>

<header class="site-header abs">
  <div class="brand"><span class="brand-dot"></span>Brevanor</div>
  <nav class="nav">
    <a class="active">Home</a><a>About Us</a><a>Services</a><a>Testimonials</a><a>Contacts</a>
  </nav>
</header>

<section class="hero abs" role="img" aria-label="Tower crane against a warm sunset sky">
  <h1>Construction solution<br>for everyone</h1>
  <a class="btn">Start Project <span>→</span></a>
</section>

<div class="feature abs" style="left:340px;top:548px">
  <svg width="26" height="26" viewBox="0 0 26 26" fill="none" stroke="#fff" stroke-width="2"><rect x="3" y="5" width="20" height="18"/><path d="M3 10h20M8 2v6M18 2v6"/></svg>
  <h3>Save 60% of your time</h3>
  <p>Clear schedules keep every phase on track and cut delays across your project.</p>
</div>
<div class="feature dark abs" style="left:512px;top:512px">
  <svg width="26" height="26" viewBox="0 0 26 26" fill="none" stroke="#fff" stroke-width="2"><circle cx="13" cy="13" r="10"/><path d="M13 7v12M9 10h6a2 2 0 010 4h-4a2 2 0 000 4h6"/></svg>
  <h3>Save 80% of your budget</h3>
  <p>Precise planning limits rework and keeps costs within the agreed budget.</p>
</div>
<div class="feature abs" style="left:684px;top:548px">
  <svg width="26" height="26" viewBox="0 0 26 26" fill="none" stroke="#fff" stroke-width="2"><path d="M3 21l7-7 5 4 8-10M17 8h6v6"/></svg>
  <h3>Boost your business</h3>
  <p>Reliable delivery builds trust and opens the door to larger projects.</p>
</div>

<section class="about">
  <p class="eyebrow abs" style="left:272px;top:808px">About us</p>
  <h2 class="section-title abs" style="left:272px;top:826px">With our knowledge<br>we guarente success</h2>
  <p class="body-copy abs" style="left:272px;top:918px;width:360px">We are a leading provider of professional planning and scheduling services, offering our expertise to major construction projects in diverse industries. Our team of experienced professionals brings a wealth of knowledge and skill to keep every project on schedule.</p>
  <a class="btn abs" style="left:272px;top:1004px">Contact Us <span>→</span></a>
  <div class="about-mark abs"><div class="brand"><span class="brand-dot"></span>Brevanor</div></div>
</section>

<section class="services">
  <p class="eyebrow abs" style="left:272px;top:1136px">What we do</p>
  <h2 class="section-title abs" style="left:272px;top:1152px">Our Services</h2>
  <div class="service abs" style="left:272px;top:1196px"><h3>Project<br>Management</h3><p>From early studies to final handover, we lead the planning, coordination and control of complex projects so every team works to one clear plan and goal.</p></div>
  <div class="service red abs" style="left:438px;top:1196px"><h3>Project<br>Controls</h3><p>We track cost, schedule and progress in detail, flagging risk early and giving owners accurate reports to support fast and confident project decisions.</p></div>
  <div class="service abs" style="left:604px;top:1196px"><h3>Contract<br>Management</h3><p>We manage contracts, claims and changes with care, protecting your interests and keeping every party aligned with the scope, terms and deadlines agreed.</p></div>
  <div class="service red abs" style="left:770px;top:1196px"><h3>Procurement<br>Managment</h3><p>We plan and follow the purchase of equipment and materials so long lead items arrive on time and fit the construction sequence without delay.</p></div>
</section>

<section class="testimonials">
  <p class="eyebrow abs" style="left:0;top:1490px;width:1200px;text-align:center">Testimonials</p>
  <h2 class="section-title abs" style="left:0;top:1506px;width:1200px;text-align:center;font-size:30px">Our Clients Say</h2>
  <div class="client-photo abs" role="img" aria-label="Construction worker on a site against a blue sky"></div>
  <div class="quote-box abs"><svg width="18" height="14" viewBox="0 0 18 14" fill="#fff"><path d="M0 14V7L4 0h3L5 6h3v8zM10 14V7l4-7h3l-2 6h3v8z"/></svg></div>
  <p class="body-copy abs" style="left:600px;top:1580px;width:328px">Brevanor gave our mining project the structure it needed. Their planners built a clear schedule, tracked every milestone and helped us finish ahead of the deadline with costs under control.</p>
  <p class="head abs" style="left:600px;top:1686px;font-size:13px;font-weight:600">Marc Delorin</p>
  <p class="abs" style="left:600px;top:1704px;font-size:9px;color:var(--red)">Project Director</p>
  <div class="dots abs" style="left:600px;top:1726px"><span class="on"></span><span></span><span></span></div>
</section>

<section class="contact">
  <p class="eyebrow abs" style="left:272px;top:1818px">Contact form</p>
  <h2 class="section-title abs" style="left:272px;top:1836px;font-size:30px">Lets be in touch</h2>
  <div class="field abs" style="left:272px;top:1900px;width:174px">First Name</div>
  <div class="field abs" style="left:456px;top:1900px;width:176px">Last Name</div>
  <div class="field abs" style="left:272px;top:1944px;width:174px">Email</div>
  <div class="field abs" style="left:456px;top:1944px;width:176px">Select Service <span>▾</span></div>
  <div class="field area abs" style="left:272px;top:1988px;width:360px">Your Text</div>
  <a class="btn abs" style="left:272px;top:2096px;padding:10px 20px">Send <span>→</span></a>

  <div class="contact-item abs" style="left:272px;top:2164px"><span class="icon-circle"><svg width="12" height="10" viewBox="0 0 12 10" fill="none" stroke="#fff" stroke-width="1.4"><rect x="1" y="1" width="10" height="8"/><path d="M1 1l5 4 5-4"/></svg></span><span>Email Address<br>hello@brevanor.ca<br>projects@brevanor.ca</span></div>
  <div class="contact-item abs" style="left:456px;top:2164px"><span class="icon-circle"><svg width="12" height="12" viewBox="0 0 12 12" fill="#fff"><path d="M2 1h3l1 3-2 1a7 7 0 003 3l1-2 3 1v3c-6 0-10-4-10-9z"/></svg></span><span>Contact Number<br>+1 514 555 0142<br>+1 514 555 0178</span></div>

  <div class="map abs" role="img" aria-label="Street map of the office location">
    <svg style="position:absolute;left:120px;top:110px" width="28" height="36" viewBox="0 0 28 36"><path d="M14 0C6 0 0 6 0 14c0 10 14 22 14 22s14-12 14-22C28 6 22 0 14 0z" fill="var(--red)"/><circle cx="14" cy="14" r="5" fill="#fff"/></svg>
  </div>
  <div class="address-card abs">
    <p style="font-size:9px;color:var(--muted)">Company Address</p>
    <p class="head" style="font-size:17px;font-weight:600;line-height:22px;margin-top:6px">H3B 2Y5, 880 Rue Calder,<br>Montreal, Canada</p>
  </div>
</section>

<footer class="site-footer abs">
  <div class="brand"><span class="brand-dot"></span>Brevanor</div>
  <p class="copy">© Brevanor. All rights reserved. Copyright 2023</p>
  <nav class="nav"><a>About Us</a><a>Services</a><a>Testimonials</a><a>Contacts</a></nav>
</footer>

</body>
</html>
```